Book Title: “Ember: Trail of Quiet Wonder” Please see the attachment “Text on the cover”.

Book Cover Design Instructions: This book is meant for people of all religions and nationalities. Therefore, on the cover, there should be no mosque or an object specific to any religion. The primary emphasis should be on the "unconditional love of God." Therefore, use universal symbols of love. The second priority themes could be Sufism, Peace, and self-improvement. Rest is your imagination. Please also see the attachment: 'Book description and author's Bio.'
This book has the potential to be a best seller. Please do a good job.
What Book Cover Formats are required: A designer should submit cover designs in three formats: (1) eBook, (2) Paperback, and (3) Hardback. These books will be published on Quillory RTS.
Format requirements for eBooks are available from: https://rts.quillory-books.example/en_US/help/topic/H384017265.
You can find paperback and hardback cover measurements from: https://rts.quillory-books.example/en_US/cover-calculator
• To complete the project, all three formats should be accepted by Quillory RTS.
• The book interior trim size is 6.14 X 9.21 inches.
• Interior Type: Premium color.
• No bleed.
• I do not upload barcode. So, the back cover should have room for Quillory to print the barcode.
• Number of pages 126.
Compensation for the designer: After selecting one designer, I will increase the amount by $200 on Brieflane to compensate for three deliverables.
Follow-up of the Project:
After the book is published, I may need minor revisions. For example, the number of pages may change. Therefore, I will need the same design in revised sizes. In that case, I will pay $25 for each revision. For example, if the number of pages changes, I will need a different spine for paperback and hardback, then I will pay the artist $25 + $25 = $50 for both designs.
List of Enclosers:
1. Text on the cover.
2. Book description and author's Bio for the back cover.
3. Later, I will upload my picture for the book's back cover.

Any adult

Any industry

• Three Deliverables

```html
<!DOCTYPE html>
<html lang="en">
<head>
<meta charset="utf-8">
<title>Ember: Trail of Quiet Wonder — Book Cover Wrap</title>
<link href="https://fonts.googleapis.com/css2?family=Cinzel:wght@400;600;700&family=Crimson+Text:ital,wght@0,400;0,600;1,600;1,700&display=swap" rel="stylesheet">
<style>
  :root {
    --gold: #d6ae5c;
    --cream: #fbf6ec;
    --ink-dark: #0e0805;
    --umber: #3a2414;
    --amber: #a8783c;
    --glow: #f3dcaa;
    --placeholder: #ababab;
    --rule: #8a7a5a;
    --page: #ffffff;
  }
  * { box-sizing: border-box; margin: 0; padding: 0; }
  html, body {
    width: 1200px; height: 844px; overflow: hidden; background: var(--page);
  }
  .wrap {
    position: absolute; left: 22px; top: 22px; width: 1156px; height: 800px;
    overflow: hidden; border: 1px solid #2a1a10;
  }
  .cover-photo {
    position: absolute; inset: 0;
    background:
      radial-gradient(ellipse 260px 330px at 900px 420px, var(--glow) 0%, rgba(214,170,100,0.75) 40%, rgba(120,80,40,0) 100%),
      linear-gradient(90deg, var(--ink-dark) 0%, #1a0f08 40%, var(--umber) 52%, #6a4626 65%, var(--amber) 85%, #7a5430 100%);
  }
  .spine-edge {
    position: absolute; top: 0; bottom: 0; width: 1px; background: var(--rule);
  }
  .spine-edge--left { left: 534px; }
  .spine-edge--right { left: 622px; }

  .title {
    position: absolute; font-family: "Cinzel", serif; color: var(--gold);
    text-align: center; line-height: 1; font-weight: 400;
  }
  .subtitle-caps {
    position: absolute; font-family: "Cinzel", serif; color: var(--cream);
    text-align: center; line-height: 1;
  }
  .author {
    position: absolute; font-family: "Cinzel", serif; color: var(--gold);
    text-align: center; line-height: 1; white-space: nowrap;
  }

  /* Back cover */
  .back-title { left: 109px; top: 52px; width: 316px; font-size: 106px; }
  .back-subtitle { left: 109px; top: 136px; width: 316px; font-size: 26px; font-variant: small-caps; letter-spacing: 0.5px; }
  .blurb {
    position: absolute; left: 61px; top: 175px; width: 412px;
    font-family: "Crimson Text", serif; color: var(--cream);
    font-size: 13px; line-height: 14.8px; text-align: justify; hyphens: auto;
  }
  .back-byline {
    position: absolute; left: 61px; top: 435px; width: 404px; height: 26px;
    display: flex; align-items: center; gap: 12px;
  }
  .back-byline .rule { flex: 1; height: 1px; background: var(--gold); }
  .back-byline .author { position: static; font-size: 22px; font-variant: small-caps; }
  .author-portrait {
    position: absolute; left: 63px; top: 472px; width: 124px; height: 158px;
    background: var(--placeholder);
  }
  .bio {
    position: absolute; left: 197px; top: 471px; width: 276px;
    font-family: "Crimson Text", serif; color: var(--cream);
    font-size: 13px; line-height: 14.8px; text-align: justify;
  }
  .barcode-space {
    position: absolute; left: 308px; top: 655px; width: 160px; height: 96px;
    border: 1px solid #9a9a9a;
  }

  /* Spine */
  .spine-text {
    position: absolute; writing-mode: vertical-rl; white-space: nowrap;
  }
  .spine-title { left: 553px; top: 55px; font-family: "Cinzel", serif; color: var(--gold); font-size: 66px; line-height: 1; }
  .spine-subtitle { left: 555px; top: 295px; font-family: "Cinzel", serif; color: var(--cream); font-size: 24px; line-height: 24px; font-variant: small-caps; }
  .spine-author { left: 572px; top: 531px; font-family: "Cinzel", serif; color: var(--cream); font-size: 25px; line-height: 1; font-variant: small-caps; }

  /* Front cover */
  .front-title { left: 644px; top: 43px; width: 470px; font-size: 150px; }
  .front-subtitle { left: 644px; top: 177px; width: 470px; font-size: 38px; font-weight: 700; text-shadow: 0 2px 6px rgba(40,20,5,0.5); }
  .tagline {
    position: absolute; left: 644px; top: 684px; width: 470px;
    font-family: "Crimson Text", serif; font-style: italic; font-weight: 700;
    color: var(--cream); font-size: 23px; line-height: 25px; text-align: center;
    text-shadow: 0 1px 4px rgba(40,20,5,0.6);
  }
  .front-author { left: 644px; top: 746px; width: 470px; font-size: 33px; font-weight: 600; font-variant: small-caps; text-shadow: 0 1px 4px rgba(40,20,5,0.5); }
</style>
</head>
<body>
  <main class="wrap">
    <div class="cover-photo" role="img" aria-label="Warm sunlit scene: a figure in quiet prayer beneath a glowing arch, rays of light falling across a stone floor and into the dark back cover"></div>
    <div class="spine-edge spine-edge--left"></div>
    <div class="spine-edge spine-edge--right"></div>

    <section class="back-cover">
      <h2 class="title back-title">EMBER</h2>
      <p class="subtitle-caps back-subtitle">Trail of Quiet Wonder</p>
      <div class="blurb">
        <p>Lorem ipsum dolor sit amet, consectetuer adipiscing elit, sed diam nonummy nibh euismod tincidunt ut laoreet dolore magna aliquam erat volutpat. Ut wisi enim ad minim veniam, quis nostrud exerci tation ullamcorper suscipit lobortis nisl ut aliquip ex ea commodo consequat. Duis autem vel eum iriure dolor in hendrerit in vulputate velit esse molestie consequat, vel illum dolore eu feugiat nulla facilisis at vero eros et accumsan et iusto odio dignissim qui blandit praesent luptatum zzril delenit augue duis dolore te feugait nulla facilisi.</p>
        <p>Lorem ipsum dolor sit amet, cons ectetuer adipiscing elit, sed diam nonummy nibh euismod tincidunt ut laoreet dolore magna aliquam erat volutpat. Ut wisi enim ad minim veniam, quis nostrud exerci tation ullamcorper suscipit lobortis nisl ut aliquip ex ea commodo consequat.</p>
        <p>Lorem ipsum dolor sit amet, consectetuer adipiscing elit, sed diam nonummy nibh euismod tincidunt ut laoreet dolore magna aliquam erat volutpat. Ut wisi enim ad minim veniam, quis nostrud exerci tation ullamcorper suscipit lobortis nisl ut aliquip ex ea commodo consequat. Duis autem vel eum iriure dolor in hendrerit in</p>
      </div>
      <div class="back-byline">
        <span class="rule"></span>
        <span class="author">Dr. Ilyan Sorrel</span>
        <span class="rule"></span>
      </div>
      <div class="author-portrait" role="img" aria-label="Author portrait"></div>
      <p class="bio">Lorem ipsum dolor sit amet, consectetuer adipiscing elit, sed diam nonummy nibh euismod tincidunt ut laoreet dolore magna aliquam erat volutpat. Ut wisi enim ad minim veniam, quis nostrud exerci tation ullamcorper suscipit lobortis nisl ut aliquip ex ea commodo consequat. Duis autem vel eum iriure dolor in hendrerit in vulputate velit esse molestie consequat, vel illum dolore eu feugiat nulla facilisis at vero eros et accumsan et iusto odio dignissim qui blandit praesent luptatum zzril delenit augue duis dolore te feugait nulla facilisi.</p>
      <div class="barcode-space"></div>
    </section>

    <section class="spine">
      <span class="spine-text spine-title">EMBER</span>
      <span class="spine-text spine-subtitle">Trail of<br>Quiet Wonder</span>
      <span class="spine-text spine-author">Dr. Ilyan Sorrel</span>
    </section>

    <section class="front-cover">
      <h1 class="title front-title">EMBER</h1>
      <p class="subtitle-caps front-subtitle">TRAIL OF QUIET WONDER</p>
      <p class="tagline">Guide to Cultivating Inner Peace<br>and Mindful Living</p>
      <p class="author front-author">Dr. Ilyan Sorrel</p>
    </section>
  </main>
</body>
</html>
```